"Precision Solutions for Aerospace Industries" product catalog Brennicor

General Catalog Guidelines
Format: A4, in vertical or horizontal orientation.
Cover Page: Should include the company logo, slogan, and website address (e.g., www.brennicor-example.com).
Layout: Each page can feature 1, 2, or up to 3 products, ensuring clarity and readability.
Catalog Content
1. Title Page
Catalog Name: "Technical Consumables for Aerospace".
Company Logo: BrenniCor.
High-Quality Image: Related to the aerospace industry.
2. Table of Contents
List of sections with corresponding page numbers for easy navigation.
3. Introduction / Scope of Activities
Company Overview: Brief introduction to BrenniCor's operations.
Specialization: Emphasis on manufacturing spare parts and consumables for special processes such as thermal spraying, diffusion brazing, welding, etc.
Certifications: Company certifications (AS9100, military concession) and a list of major clients.
Mission: "Brennicor's mission is to meet the requirements of thermal spray and aviation industry customers by continuous improvement of employees' qualifications, machining of difficult-to-machine materials using modern and non-conventional manufacturing processes, and new implementations of technological processes using developed know-how."
Vision: "To be a recognizable brand in the thermal spray and aviation industry on the global market. Be not only associated with the manufacturing of parts under the customers' purchase orders but also with innovative solutions that will bring many benefits to the contractor."
4. Key Sections of the Catalog
Consumables for Special Processes

Test coupons, panels, samples, and other elements for thermal spraying, chemical processing, welding.
Machining of difficult-to-machine materials such as nickel and cobalt-based superalloys, titanium, and hardened steel.
Reusable silicone masking and other masking solutions.
Coupons Regeneration

Description of the coupon regeneration process and its benefits (material savings, cost reduction, environmental impact).
Metal Parts and PSP Prefabricates

Structural elements, e.g., honeycombs, repair parts for turbines, ready-made PSP elements.
Machining and Support Services

Wire EDM cutting – benefits and applications.
Coating evaluation laboratory and technological accessories.
Consultations on technological processes, preparation for QUALTEX certification.
Modern Aviation Materials

Ceramic composites (CMC), nickel and cobalt-based superalloys, and other aerospace materials.
Repair and R&D Services

Examples of research and development projects (e.g., repair of Varnel 53 airfoils).
Solutions for issues related to thermal spraying and process optimization.
Additional Information

Information on hybrid additive manufacturing.
Current company status and client list.
5. Last Page
Contact Information:
Production Site: Wiktora Grabca 12, 05-410 Otwock, Poland.
R&D Center: Brzozówka 318B, 36-014 Brzozówka, Poland.
Email address, phone number, and social media links.
"Nice to Have" Elements
Inspirational Images: Products in use, e.g., aerospace tests, industrial applications
Updates

Project details can be found at this link https://files.example-share.net/t-KmQ4rwzLxa

Target Market(s)

aviation industry, metallurgy

Industry/Entity Type

Font styles to use
Sans Serif

Colors
0054AA
0677BA
7BADD7
CADEEF
E8F1F8
F0912C
F2A743
F7CA91
FBE8D2
FDF5EE

Requirements
Must have
• 1. Cover Eye-catching graphics. Your company logo. A short, clear title (e.g. catalog name, season, offer). 2. Table of contents Particularly important in larger catalogs. Makes it easier to quickly find individual sections. 3. Introduction / Company information A short company mission or introduction (information at https://brennicor-example.com/about-us/) 4. Key categories and sections Division into easy-to-understand sections, e.g.: Products, Services. 5. Product pages; 8. Aesthetics and readability Use colors consistent with the brand's visual identification. Consistent fonts and text hierarchy (e.g. titles larger than descriptions). Well-placed elements on the page so as not to overwhelm the viewer.
Nice to have
• Lifestyle inspirations and photos Photos from the industry such as: airplanes, turbines, lathe machines, WEDEM.

```html
<!DOCTYPE html>
<html lang="en">
<head>
<meta charset="utf-8">
<title>BrenniCor Catalog – Services Spread</title>
<link href="https://fonts.googleapis.com/css2?family=Montserrat:wght@500;600;700&display=swap" rel="stylesheet">
<style>
  :root {
    --backdrop: #8c8c8c;
    --paper: #ffffff;
    --brand-blue: #2e55a5;
    --ink: #1e1e24;
    --panel: #f1f2f5;
    --sky-top: #e9eef2;
    --sky-bottom: #f4f6f8;
    --gutter-shade: rgba(0, 0, 0, 0.06);
  }
  * { box-sizing: border-box; margin: 0; padding: 0; }
  html, body { width: 1200px; height: 1126px; overflow: hidden; }
  body {
    background: var(--backdrop);
    font-family: "Montserrat", sans-serif;
    color: var(--ink);
    position: relative;
  }
  .spread {
    position: absolute;
    left: 52px; top: 180px;
    width: 1096px; height: 740px;
    background: var(--paper);
  }
  .page { position: absolute; top: 0; height: 740px; }
  .page--left {
    left: 0; width: 541px;
    background: linear-gradient(to right, var(--paper) 0, var(--paper) 505px, var(--gutter-shade) 541px);
  }
  .page--right { left: 541px; width: 555px; }

  .brand {
    position: absolute; left: 330px; top: 50px;
    display: flex; align-items: center; gap: 6px;
    font-weight: 700; font-size: 18px; letter-spacing: 0.2px;
    color: var(--brand-blue);
  }
  .brand__mark { width: 14px; height: 14px; background: var(--brand-blue); }

  .section { position: absolute; left: 47px; }
  .section__title {
    font-weight: 700; font-size: 17.5px; line-height: 19.5px;
    color: var(--brand-blue); text-transform: uppercase;
  }
  .section__lead {
    font-size: 7px; font-weight: 500; line-height: 9px;
    margin-top: 14px; width: 260px;
  }
  .checklist { list-style: none; margin-top: 10px; }
  .checklist li {
    position: relative; padding-left: 14px;
    font-size: 7px; font-weight: 500; line-height: 10.5px;
    margin-bottom: 4px;
  }
  .checklist li svg { position: absolute; left: 1px; top: 1.5px; width: 8px; height: 8px; }
  .sublist { list-style: none; margin: 4px 0 2px 26px; }
  .sublist li { padding-left: 12px; margin-bottom: 2px; line-height: 9px; }
  .sublist li::before {
    content: ""; position: absolute; left: 0; top: 3px;
    width: 4px; height: 4px; border-radius: 50%; background: var(--brand-blue);
  }
  .checklist--tight li { margin-bottom: 5.5px; }

  .visual { position: absolute; border-top-left-radius: 30px; }
  .visual--spray { left: 338px; top: 107px; width: 158px; height: 132px; background: var(--panel); }
  .visual--quality { left: 350px; top: 289px; width: 146px; height: 161px; background: var(--panel); }
  .visual--aircraft {
    left: 312px; top: 497px; width: 184px; height: 186px;
    background: linear-gradient(to bottom, var(--sky-top), var(--sky-bottom));
  }

  .rule {
    position: absolute; left: 50px; width: 446px; height: 4px;
    border-top: 1px solid var(--brand-blue); border-bottom: 1px solid var(--brand-blue);
  }
  .rule--one { top: 262px; }
  .rule--two { top: 468px; }

  .chapter-title {
    position: absolute; left: 0; width: 555px; top: 298px;
    text-align: center; font-weight: 700;
    font-size: 40px; line-height: 37px; color: var(--brand-blue);
  }
  .chapter-rule {
    position: absolute; left: 188px; top: 398px; width: 266px;
  }
  .chapter-rule span { display: block; height: 1px; background: var(--brand-blue); margin-bottom: 2.5px; }
</style>
</head>
<body>
<svg width="0" height="0" style="position:absolute">
  <defs>
    <symbol id="tick" viewBox="0 0 16 16">
      <circle cx="8" cy="8" r="8" fill="#2e55a5"/>
      <path d="M4.3 8.3l2.5 2.4 4.9-5.2" fill="none" stroke="#fff" stroke-width="2" stroke-linecap="round" stroke-linejoin="round"/>
    </symbol>
  </defs>
</svg>

<main class="spread">
  <section class="page page--left">
    <div class="brand"><span class="brand__mark"></span>BRENNICOR</div>

    <article class="section" style="top:54px">
      <h2 class="section__title">Thermal Spray<br>/ Plasma Spray<br>Problem Solving Services</h2>
      <p class="section__lead">Our experience in thermal processes, mainly in Plasma Spraying allows for comprehensive optimization from the side of:</p>
      <ul class="checklist" style="width:250px">
        <li><svg><use href="#tick"/></svg>Design of technological equipment i.e., fixtures</li>
        <li><svg><use href="#tick"/></svg>Masking, as an aid in the selection of the most favorable solutions to protect the part from overspray and sandblasting</li>
        <li><svg><use href="#tick"/></svg>coating quality assurance solutions, consultations for control and technical plans, conducting the first article inspection (FAI) and pre- audit for QUALTEX accreditation.</li>
      </ul>
    </article>
    <div class="visual visual--spray" role="img" aria-label="Illustration of a robotic arm spraying coating onto a part"></div>

    <div class="rule rule--one"></div>

    <article class="section" style="top:290px">
      <h2 class="section__title">Services Related to<br>Quality Management</h2>
      <p class="section__lead">Consulting, audits, preparation for certification, training for implementation and maintenance of:</p>
      <ul class="checklist" style="width:262px">
        <li><svg><use href="#tick"/></svg>Technological processes requiring QUALTEX accreditation (including, but no limited to Coatings PRI AC7109 - thermal spray, Coating Evaluation Laboratory, Stripping of Coatings)</li>
        <li><svg><use href="#tick"/></svg>First article inspection (FAI) according to AS9102</li>
        <li><svg><use href="#tick"/></svg>Quality Management System compliant with ISO9001 / AS9100 and PRI AC7004 (QUALTEX Aerospace Quality System)</li>
        <li><svg><use href="#tick"/></svg>Control and technical plans for special processes</li>
      </ul>
    </article>
    <div class="visual visual--quality" role="img" aria-label="Illustration of a checklist clipboard"></div>

    <div class="rule rule--two"></div>

    <article class="section" style="top:488px">
      <h2 class="section__title">Quality Assurance<br>According to AS9100</h2>
      <ul class="checklist checklist--tight" style="width:250px;margin-top:8px">
        <li><svg><use href="#tick"/></svg>Working with technological standards/specifications describing:
          <ul class="sublist">
            <li style="position:relative">production requirements regarding the equipment, staff and the process itself</li>
            <li style="position:relative">Raw material properties</li>
          </ul>
        </li>
        <li><svg><use href="#tick"/></svg>CMM measurements</li>
        <li><svg><use href="#tick"/></svg>First Article Inspection (FAI) according to AS9102</li>
        <li><svg><use href="#tick"/></svg>Control and technical plans for special processes</li>
        <li><svg><use href="#tick"/></svg>Technological Validation for each manufacturing process</li>
        <li><svg><use href="#tick"/></svg>QUALTEX best practices implemented in manufacturing processes</li>
        <li><svg><use href="#tick"/></svg>Materials and coatings properties testing</li>
        <li><svg><use href="#tick"/></svg>Statistical Process Control for production</li>
      </ul>
    </article>
    <div class="visual visual--aircraft" role="img" aria-label="Photo of a passenger airliner climbing above clouds with faint AS9100 lettering"></div>
  </section>

  <section class="page page--right">
    <h1 class="chapter-title">SPACE<br>APPLICATION</h1>
    <div class="chapter-rule"><span></span><span></span><span></span><span></span></div>
  </section>
</main>
</body>
</html>
```